A new novel about the early days of The Marlows needs a book cover design

The title of the book is A LANTERN IN WINTER
The cover should also include "a novel" and "by Tom Holloway" Those can be together or separate.
The design element I'd like to incorporate is the iconic "Dock Wall" photo of The Marlows in 1960, which I've attached below. Since we're not sure if we can get the rights to the actual photo, it's probably best if the design merely references that photo, or distorts it in an interesting way. But it should be very clear that the book is about the Marlows.
The novel is in many ways based on that photo and evokes the city of Hamburg in 1960, which was gritty, raw, and sexually charged (as were The Marlows).
The tone of the novel is romantic, passionate, and very funny - but never broad and silly.

```html
<!DOCTYPE html>
<html lang="en">
<head>
<meta charset="utf-8">
<title>A Lantern in Winter — Tom Holloway</title>
<link rel="stylesheet" href="https://fonts.googleapis.com/css2?family=Stardos+Stencil:wght@700&family=Open+Sans:wght@300;400&display=swap">
<style>
  :root {
    --navy: #1c2335;
    --orange: #ff7f00;
    --orange-deep: #d96a00;
  }
  * { margin: 0; padding: 0; box-sizing: border-box; }
  html, body {
    width: 840px;
    height: 1200px;
    overflow: hidden;
    background: var(--navy);
  }
  .filters { position: absolute; width: 0; height: 0; overflow: hidden; }
  .cover {
    position: relative;
    width: 840px;
    height: 1200px;
    background: var(--navy);
    color: var(--orange);
    text-align: center;
  }
  .band-photo {
    position: absolute;
    left: 0;
    top: 0;
    width: 840px;
    height: 440px;
    background:
      linear-gradient(180deg,
        rgba(28,35,53,0) 0%,
        rgba(28,35,53,0) 44%,
        rgba(28,35,53,0.85) 58%,
        var(--navy) 70%,
        rgba(28,35,53,0.55) 88%,
        rgba(28,35,53,0.7) 93%,
        var(--navy) 100%),
      linear-gradient(90deg,
        var(--orange) 0%, var(--orange-deep) 18%, var(--orange) 30%,
        var(--orange-deep) 47%, var(--orange) 60%, var(--orange-deep) 76%,
        var(--orange) 88%, var(--orange-deep) 100%);
    filter: url(#distress-soft);
  }
  .title {
    position: absolute;
    left: 0;
    top: 494px;
    width: 840px;
    font-family: "Stardos Stencil", "Courier New", serif;
    font-weight: 700;
    line-height: 1;
    text-transform: uppercase;
    -webkit-text-stroke: 2px var(--orange);
    filter: url(#distress);
  }
  .title-top {
    display: block;
    font-size: 92px;
    letter-spacing: -2px;
  }
  .title-main {
    display: block;
    margin-top: 2px;
    font-size: 138px;
    letter-spacing: -4px;
  }
  .genre {
    position: absolute;
    left: 0;
    top: 780px;
    width: 840px;
    font-family: "Open Sans", Arial, sans-serif;
    font-weight: 400;
    font-size: 33px;
  }
  .author {
    position: absolute;
    left: 0;
    top: 1082px;
    width: 840px;
    font-family: "Open Sans", Arial, sans-serif;
    font-weight: 300;
    font-size: 55px;
    letter-spacing: 10px;
    padding-left: 10px;
  }
</style>
</head>
<body>
  <svg class="filters" aria-hidden="true">
    <filter id="distress" x="0" y="0" width="100%" height="100%">
      <feTurbulence type="fractalNoise" baseFrequency="0.08" numOctaves="3" seed="7" result="noise"/>
      <feColorMatrix in="noise" type="matrix" values="0 0 0 0 0  0 0 0 0 0  0 0 0 0 0  0 0 0 -14 8.4" result="holes"/>
      <feComposite in="SourceGraphic" in2="holes" operator="in"/>
    </filter>
    <filter id="distress-soft" x="0" y="0" width="100%" height="100%">
      <feTurbulence type="fractalNoise" baseFrequency="0.05" numOctaves="3" seed="2" result="noise"/>
      <feColorMatrix in="noise" type="matrix" values="0 0 0 0 0  0 0 0 0 0  0 0 0 0 0  0 0 0 -10 6.6" result="grit"/>
      <feComposite in="SourceGraphic" in2="grit" operator="in"/>
    </filter>
  </svg>
  <main class="cover">
    <div class="band-photo" role="img" aria-label="High-contrast orange and navy duotone photograph of the Marlows, five young musicians with guitars and a drum kit, playing against the Dock Wall in 1960"></div>
    <h1 class="title">
      <span class="title-top">A Lantern</span>
      <span class="title-main">In Winter</span>
    </h1>
    <p class="genre">A NOVEL</p>
    <p class="author">TOM HOLLOWAY</p>
  </main>
</body>
</html>
```